Ledgerwise 540 for Tavlo

We are looking to design a page for the mobile app. The app is intended for financial professionals and is based on a successful desktop application. The existing design will serve as a very rough guideline, but we are open to hearing ideas.
Uploaded file #1 contains a screenshot of the existing design. The workflow is as follows:
The user picks a portfolio from the Dropdown below portfolio.
The user picks a Loss Threshold, which will dictate what gets onto the bubble chart below.
Once the bubble on the chart is clicked, a text box pops up with the description of the particular crisis that the bubble represents.
Once the bubble is clicked, the right hand side bar charts are populated with moves relevant to this scenario.
The left hand pane contains two text boxes. The lower one is particularly important, because the user is able to remove scenarios or add scenarios (screen #2). Removing scenarios is simple.
Adding scenarios brings up a wizard (screen #3). It also needs to be designed consistently with the front page of the app. The wizard has different clickable categories going down the column on the left and in a row on the top. The user can pick some or all of these categories.

Notes: The app should be designed for landscape mode only. The key to keep in mind is how the user will select bubbles on the chart. Right now, it is quite easy, but with the touchscreen it may be more complicated, so please keep that in mind when designing the chart (it should still be some version of the similar chart).
*As a first pass, please submit your idea of the concept (layout/colors/buttons) without the detailed design. We will choose 1-3 concepts and then the detailed work will take place with a much higher chance of a payout.
Updates

Thank you for the first two sketches. The second one by bertrand appears to be a bit more mobile app oriented, though we are still considering both and waiting for other submissions. One request, could you rework the sketches to include a bit more of dark blue as a background?  \

Bertrand, I think that the bubbles are too small and they are missing some volume effects. Could you make them a bit more prominent (and pick some form of dark blue background) and change the color to see if they will stand out better?
 

Industry/Entity Type

Financial

Requirements
Must have
• The general outline for the bubble chart must be retained. But the actual execution may differ significantly. We are open to seeing different ideas.
The winning design will also get a contract to design the rest of the application (2 more screens), which will be worth the same as the original design.

```html
<!DOCTYPE html>
<html lang="en">
<head>
<meta charset="utf-8">
<title>Ledgerwise 540 – Scenario Dashboard</title>
<link href="https://fonts.googleapis.com/css2?family=Arimo:wght@400;700&display=swap" rel="stylesheet">
<style>
:root{
  --page:#e4e4e4;
  --nav-top:#3aa6e6;
  --nav-bot:#0a6fb8;
  --nav-line:#7cc4ef;
  --tile-top:#f2f2f2;
  --tile-bot:#d6d6d6;
  --chart-bg:#243567;
  --chart-grid:#34488a;
  --axis-text:#0b0f22;
  --green:#2f9b3a;
  --green-light:#7ccf3a;
  --red:#d62a24;
  --red-dark:#a5141a;
  --tip-green:#7ab82a;
  --row-a:#eef1f4;
  --row-b:#dfe5eb;
  --highlight:#f5b800;
  --text:#1a1a1a;
  --muted:#555;
}
*{box-sizing:border-box;margin:0;padding:0}
html,body{width:1200px;height:1000px;overflow:hidden;background:var(--page);font-family:"Arimo",Arial,sans-serif;color:var(--text)}
.screen{position:absolute;left:0;top:60px;width:880px;height:646px;transform:scale(1.3636);transform-origin:0 0;background:#fff;overflow:hidden}
.abs{position:absolute}

.nav{left:0;top:0;width:880px;height:33px;display:flex;background:linear-gradient(var(--nav-top),var(--nav-bot))}
.nav-item{height:33px;display:flex;align-items:center;justify-content:center;color:#fff;font-weight:700;font-size:13px;border-right:1px solid var(--nav-line)}
.brand{flex:1;color:#fff;font-weight:700;font-size:16px;display:flex;align-items:center;justify-content:center}

.portfolio-name{left:0;top:42px;width:268px;height:54px;background:linear-gradient(#f7f7f7,#d9d9d9);display:flex;align-items:center;justify-content:center;font-weight:700;font-size:19px}
.section-head{left:0;width:268px;height:18px;background:linear-gradient(var(--nav-top),var(--nav-bot));color:#fff;font-weight:700;font-size:10.5px;display:flex;align-items:center;justify-content:center}
.bar-panel{left:0;width:268px;height:190px;background:#fff}
.bar-frame{position:absolute;left:118px;top:4px;width:145px;height:168px}
.bar-frame.high{border:1px solid var(--green-light)}
.bar-frame.low{border:1px solid var(--red)}
.gridline{position:absolute;top:0;bottom:0;width:1px;background:#d0d0d0}
.bar-row{position:absolute;left:0;width:268px;height:13px;display:flex;align-items:center}
.bar-label{width:72px;text-align:right;font-size:7.5px;font-weight:700;padding-right:3px;white-space:nowrap}
.bar-date{width:45px;font-size:7px;white-space:nowrap}
.bar{height:10px;margin-left:1px;color:#fff;font-size:7.5px;display:flex;align-items:center;justify-content:flex-end;padding-right:3px;border-radius:0 3px 3px 0}
.bar.pos{background:linear-gradient(90deg,var(--green-light),var(--green))}
.bar.neg{background:linear-gradient(90deg,#f06b60,var(--red))}
.bar.neg.deep{background:linear-gradient(90deg,var(--red),var(--red-dark))}
.bar-axis{position:absolute;top:176px;font-size:6.5px;transform:translateX(-50%)}

.chart{left:270px;top:40px;width:501px;height:488px;background:var(--chart-bg)}

.side{left:773px;top:40px;width:107px}
.tile{height:58px;margin-bottom:2px;background:linear-gradient(var(--tile-top),var(--tile-bot));display:flex;flex-direction:column;align-items:center;justify-content:center;text-align:center}
.tile-label{font-size:10px;color:var(--muted)}
.tile-value{font-size:12.5px;font-weight:700}
.tile-sub{font-size:9.5px;color:var(--muted);font-weight:700}
.tile.soft{background:#ececec;height:62px}
.tile.search{height:57px;background:#e9e9e9;justify-content:flex-start;padding-top:8px}
.search-box{margin-top:6px;width:96px;height:26px;background:#fff;border-radius:5px;position:relative}

.table-head{top:535px;height:18px;background:linear-gradient(var(--nav-top),var(--nav-bot));color:#fff;font-weight:700;font-size:10.5px;display:flex;align-items:center;justify-content:center}
.table{top:553px;font-size:11.5px}
.table-row{height:18px;display:flex;align-items:center;border-bottom:1px solid #c7ced6}
.table-row.cols{background:#fff;height:19px}
.table-row:nth-child(even){background:var(--row-a)}
.table-row:nth-child(odd):not(.cols){background:var(--row-b)}
.table-row.active{background:var(--highlight)!important}
.cell{padding-left:6px;height:100%;display:flex;align-items:center;border-right:1px solid #fff}
.num{justify-content:center;padding-left:0}
.pm{position:absolute;top:2px;width:22px;height:15px;background:#dcdcdc;color:#333;font-weight:700;font-size:13px;display:flex;align-items:center;justify-content:center}
</style>
</head>
<body>
<div class="screen">

  <nav class="nav abs">
    <div class="nav-item" style="width:118px">NEW TAB</div>
    <div class="nav-item" style="width:129px">CURRENT TAB</div>
    <div class="nav-item" style="width:111px">SAVED TAB</div>
    <div class="nav-item" style="width:83px">TOOLS</div>
    <div class="nav-item" style="width:132px">LOAD MODELS</div>
    <div class="nav-item" style="width:85px">ABOUT</div>
    <div class="nav-item" style="width:47px">?</div>
    <div class="brand">Ledgerwise 540</div>
  </nav>

  <div class="portfolio-name abs">MAM AA</div>

  <div class="section-head abs" style="top:105px">ASSET CONTRIBUTION 10 HIGHEST</div>
  <div class="bar-panel abs" style="top:123px">
    <div class="bar-frame high">
      <div class="gridline" style="left:29px"></div><div class="gridline" style="left:58px"></div>
      <div class="gridline" style="left:87px"></div><div class="gridline" style="left:116px"></div>
    </div>
    <div class="bar-row" style="top:6px"><span class="bar-label">HLM 6.505</span><span class="bar-date">02/12/67</span><span class="bar pos" style="width:121px">0.083</span></div>
    <div class="bar-row" style="top:22px"><span class="bar-label">TRX 6.02</span><span class="bar-date">02/15/67</span><span class="bar pos" style="width:103px">0.071</span></div>
    <div class="bar-row" style="top:38px"><span class="bar-label">FNVB 6.5</span><span class="bar-date">04/15/37</span><span class="bar pos" style="width:56px">0.038</span></div>
    <div class="bar-row" style="top:54px"><span class="bar-label">GRS 5.5</span><span class="bar-date">12/31/49</span><span class="bar pos" style="width:25px">0.017</span></div>
    <div class="bar-row" style="top:70px"><span class="bar-label">TDQCN 7.875</span><span class="bar-date">01/15/19</span><span class="bar pos" style="width:24px">0.016</span></div>
    <div class="bar-row" style="top:86px"><span class="bar-label">UVL Float</span><span class="bar-date">07/02/14</span><span class="bar pos" style="width:24px">0.009</span></div>
    <div class="bar-row" style="top:102px"><span class="bar-label">WRM 7.506</span><span class="bar-date">05/29/49</span><span class="bar pos" style="width:24px">0.009</span></div>
    <div class="bar-row" style="top:118px"><span class="bar-label">MERIDN 12.5</span><span class="bar-date">02/15/18</span><span class="bar pos" style="width:24px">0.002</span></div>
    <div class="bar-row" style="top:134px"><span class="bar-label">BIOX 10.25</span><span class="bar-date">10/01/15</span><span class="bar pos" style="width:24px">0.002</span></div>
    <div class="bar-row" style="top:150px"><span class="bar-label">YKC 10.25</span><span class="bar-date">02/15/16</span><span class="bar pos" style="width:24px">0.001</span></div>
    <span class="bar-axis" style="left:118px">0.00</span><span class="bar-axis" style="left:147px">0.02</span>
    <span class="bar-axis" style="left:176px">0.04</span><span class="bar-axis" style="left:205px">0.06</span>
    <span class="bar-axis" style="left:234px">0.08</span><span class="bar-axis" style="left:263px">0.10</span>
  </div>

  <div class="section-head abs" style="top:321px">ASSET CONTRIBUTION 10 LOWEST</div>
  <div class="bar-panel abs" style="top:339px">
    <div class="bar-frame low">
      <div class="gridline" style="left:29px"></div><div class="gridline" style="left:58px"></div>
      <div class="gridline" style="left:87px"></div><div class="gridline" style="left:116px"></div>
    </div>
    <div class="bar-row" style="top:6px"><span class="bar-label">WQ 7.375</span><span class="bar-date">03/15/32</span><span class="bar neg" style="width:27px">-0.320</span></div>
    <div class="bar-row" style="top:22px"><span class="bar-label">TURKEY 7</span><span class="bar-date">06/05/20</span><span class="bar neg" style="width:27px">-0.322</span></div>
    <div class="bar-row" style="top:38px"><span class="bar-label">TII 0.125</span><span class="bar-date">01/15/22</span><span class="bar neg" style="width:27px">-0.343</span></div>
    <div class="bar-row" style="top:54px"><span class="bar-label">TL 3.125</span><span class="bar-date">02/15/43</span><span class="bar neg" style="width:27px">-0.352</span></div>
    <div class="bar-row" style="top:70px"><span class="bar-label">INDON 5.875</span><span class="bar-date">03/13/20</span><span class="bar neg" style="width:27px">-0.354</span></div>
    <div class="bar-row" style="top:86px"><span class="bar-label">WAMO</span><span class="bar-date">2005-AR6 X</span><span class="bar neg" style="width:27px">-0.360</span></div>
    <div class="bar-row" style="top:102px"><span class="bar-label">RUSSIA 4.5</span><span class="bar-date">04/04/22</span><span class="bar neg" style="width:28px">-0.370</span></div>
    <div class="bar-row" style="top:118px"><span class="bar-label">TII 3/875</span><span class="bar-date">04/04/22</span><span class="bar neg" style="width:34px">-0.577</span></div>
    <div class="bar-row" style="top:134px"><span class="bar-label">TII 3.875</span><span class="bar-date">04/15/29</span><span class="bar neg" style="width:52px">-0.900</span></div>
    <div class="bar-row" style="top:150px"><span class="bar-label">AXOSA 8.6</span><span class="bar-date">12/15/30</span><span class="bar neg deep" style="width:114px">-1.975</span></div>
    <span class="bar-axis" style="left:118px">0.0</span><span class="bar-axis" style="left:147px">-0.5</span>
    <span class="bar-axis" style="left:176px">-1.0</span><span class="bar-axis" style="left:205px">-1.5</span>
    <span class="bar-axis" style="left:234px">-2.0</span><span class="bar-axis" style="left:263px">-2.5</span>
  </div>

  <svg class="chart abs" viewBox="0 0 501 488" font-family="Arimo, Arial, sans-serif" role="img" aria-label="Bubble chart of scenarios by loss and correlation surprise">
    <defs>
      <radialGradient id="bubble-red" cx="40%" cy="35%"><stop offset="0" stop-color="#ff6a5a"/><stop offset="1" stop-color="#b0140e"/></radialGradient>
      <radialGradient id="bubble-pink" cx="50%" cy="50%"><stop offset="0" stop-color="#fff"/><stop offset=".35" stop-color="#ff5fb0"/><stop offset="1" stop-color="#d01c78"/></radialGradient>
      <radialGradient id="bubble-orange" cx="50%" cy="50%"><stop offset="0" stop-color="#fff6c0"/><stop offset=".4" stop-color="#ffc02a"/><stop offset="1" stop-color="#e07a00"/></radialGradient>
    </defs>
    <rect x="33" y="15" width="447" height="448" fill="none" stroke="var(--chart-grid)"/>
    <g font-size="8" fill="var(--axis-text)" text-anchor="end">
      <text x="25" y="18">-12</text><text x="25" y="55">-13</text><text x="25" y="92">-14</text>
      <text x="25" y="130">-15</text><text x="25" y="167">-16</text><text x="25" y="205">-17</text>
      <text x="25" y="242">-18</text><text x="25" y="279">-19</text><text x="25" y="317">-20</text>
      <text x="25" y="354">-21</text><text x="25" y="391">-22</text><text x="25" y="429">-23</text>
      <text x="25" y="466">-24</text>
    </g>
    <g font-size="8" fill="var(--axis-text)" text-anchor="middle">
      <text x="33" y="478">-24</text><text x="70" y="478">-23</text><text x="108" y="478">-22</text>
      <text x="145" y="478">-21</text><text x="182" y="478">-20</text><text x="219" y="478">-19</text>
      <text x="257" y="478">-18</text><text x="294" y="478">-17</text><text x="331" y="478">-16</text>
      <text x="368" y="478">-15</text><text x="406" y="478">-14</text><text x="443" y="478">-13</text>
      <text x="480" y="478">-12</text>
    </g>
    <text x="259" y="458" font-size="7" fill="#fff" text-anchor="middle">LOSS</text>
    <text transform="translate(45,226) rotate(-90)" font-size="7" fill="#fff" text-anchor="middle">CORRELATION SURPRISE</text>

    <line x1="33" y1="340" x2="156" y2="340" stroke="#fff" stroke-width="2"/>
    <line x1="156" y1="340" x2="156" y2="463" stroke="#fff" stroke-width="2"/>

    <circle cx="81" cy="419" r="7" fill="url(#bubble-orange)"/>
    <circle cx="362" cy="165" r="7" fill="url(#bubble-pink)"/>
    <circle cx="390" cy="145" r="7" fill="url(#bubble-orange)"/>
    <circle cx="156" cy="340" r="7.5" fill="url(#bubble-red)"/>

    <g>
      <rect x="140" y="261" width="181" height="60" rx="3" fill="#fff"/>
      <path d="M140 276 V264 a3 3 0 0 1 3 -3 H318 a3 3 0 0 1 3 3 V276 Z" fill="var(--tip-green)"/>
      <path d="M152 321 L160 321 L154 330 Z" fill="#fff"/>
      <text x="230.5" y="273" font-size="10" font-weight="700" fill="#fff" text-anchor="middle">STAGFLATION SEVERE</text>
      <g font-size="9.5" font-weight="700" fill="#111" text-anchor="middle">
        <text x="230.5" y="290">Loss: -18.82</text>
        <text x="230.5" y="302">Plausibility: 0.00</text>
        <text x="230.5" y="314">Correlation Surprise: -18.82</text>
      </g>
    </g>
  </svg>

  <aside class="side abs">
    <div class="tile"><span class="tile-label">Portfolio Date</span><span class="tile-value">6/18/2013</span></div>
    <div class="tile"><span class="tile-label">Currency</span><span class="tile-value">USD</span></div>
    <div class="tile"><span class="tile-value">READ MODEL</span><span class="tile-sub">Model Date<br>06/12/2013</span></div>
    <div class="tile"><span class="tile-value">WEIGHT TYPE</span><span class="tile-sub">Active</span></div>
    <div class="tile"><span class="tile-value">VALMORA</span><span class="tile-sub">Model</span></div>
    <div class="tile"><span class="tile-value">LOSS<br>THRESHOLD</span><span class="tile-sub">-10</span></div>
    <div class="tile soft">
      <span class="tile-sub">Online Key<br>Scenarios</span>
      <svg width="14" height="12" viewBox="0 0 14 12" aria-hidden="true"><rect x=".5" y=".5" width="11" height="11" fill="#fff" stroke="#999"/><path d="M2 6 L5 9 L13 1" fill="none" stroke="#1f8ae0" stroke-width="2"/></svg>
    </div>
    <div class="tile search">
      <span class="tile-value" style="font-size:10.5px">Current Scenario</span>
      <div class="search-box">
        <svg class="abs" style="right:5px;top:5px" width="16" height="16" viewBox="0 0 16 16" aria-hidden="true"><circle cx="6.5" cy="6.5" r="4.5" fill="none" stroke="#333" stroke-width="1.6"/><line x1="10" y1="10" x2="14.5" y2="14.5" stroke="#333" stroke-width="2"/></svg>
      </div>
    </div>
  </aside>

  <div class="table-head abs" style="left:0;width:436px">SHOCKS</div>
  <div class="table abs" style="left:0;width:436px">
    <div class="table-row cols"><span class="cell" style="width:230px;padding-left:30px">Name</span><span class="cell" style="width:125px">Type</span><span class="cell num" style="width:81px">Shock</span></div>
    <div class="table-row"><span class="cell" style="width:204px;padding-left:30px">United States</span><span class="cell" style="width:151px;padding-left:27px">Equity Indexx</span><span class="cell num" style="width:81px">-15</span></div>
    <div class="table-row"><span class="cell" style="width:204px;padding-left:30px">Gold</span><span class="cell" style="width:151px;padding-left:27px">Macro/Styxxx</span><span class="cell num" style="width:81px">60</span></div>
    <div class="table-row"><span class="cell" style="width:204px;padding-left:30px">3 Years US Government</span><span class="cell" style="width:151px;padding-left:27px">Interest Ratxx</span><span class="cell num" style="width:81px">3</span></div>
    <div class="table-row"><span class="cell" style="width:204px;padding-left:30px">30 Years US Government</span><span class="cell" style="width:151px;padding-left:27px">Interest Ratxx</span><span class="cell num" style="width:81px">3</span></div>
  </div>

  <div class="table-head abs" style="left:440px;width:440px">CURRENT SCENARIO</div>
  <div class="pm" style="left:824px;top:537px">+</div>
  <div class="pm" style="left:851px;top:537px">−</div>
  <div class="table abs" style="left:440px;width:434px">
    <div class="table-row cols"><span class="cell" style="width:166px;padding-left:29px">Name</span><span class="cell num" style="width:76px">Loss</span><span class="cell num" style="width:100px">Correlation</span><span class="cell num" style="width:92px">Planxxxx</span></div>
    <div class="table-row"><span class="cell" style="width:166px;padding-left:29px">US Treasury Interest</span><span class="cell num" style="width:76px">-21.57</span><span class="cell num" style="width:100px">-21.57</span><span class="cell" style="width:92px"></span></div>
    <div class="table-row active"><span class="cell" style="width:166px;padding-left:29px">Stagflation Severe</span><span class="cell num" style="width:76px">-18.82</span><span class="cell num" style="width:100px">-18.82</span><span class="cell" style="width:92px"></span></div>
    <div class="table-row"><span class="cell" style="width:166px;padding-left:29px">Stagflation</span><span class="cell num" style="width:76px">-11.1</span><span class="cell num" style="width:100px">-11.1</span><span class="cell" style="width:92px"></span></div>
    <div class="table-row"><span class="cell" style="width:166px;padding-left:29px">US Treasury Interest</span><span class="cell num" style="width:76px">-10.87</span><span class="cell num" style="width:100px">-10.87</span><span class="cell" style="width:92px"></span></div>
  </div>

</div>
</body>
</html>
```